I need a wordpress website for myconsulting company specialized in data privacy

I'm looking for a wordpress website for my consulting company specialized in data privacy (GDPR) and computer science.
The website will serve as entry point to for potential clients.
The website should have the following sections (I'm opened to new ideas):
- Presentation of the company
- General presentation
- Services provided with some details
- Blog/articles with tags (if possible)
- Contact
On every page of the website there should be some references to pages (such as privacy policy, legal information...)
If possible he website should be multinlingual (english and french). I'll personnally take care of the translation in french.
Regarding branding;
- Name of the company: Laurent Dubreuil Conseil
- Logo is attached
- For colors to be used see attached PDF for exemple

```html
<!DOCTYPE html>
<html lang="en">
<head>
<meta charset="utf-8">
<title>Laurent Dubreuil Conseil – Website Design</title>
<link href="https://fonts.googleapis.com/css2?family=Michroma&family=Poppins:wght@400;500;600&display=swap" rel="stylesheet">
<style>
  :root{
    --board:#16828c;
    --board-light:#2596a0;
    --navy:#0e2636;
    --navy-deep:#0a1d2a;
    --teal:#1b9ba0;
    --teal-soft:#4fc3c0;
    --white:#ffffff;
    --paper:#f3f6f7;
    --ink:#1d3240;
    --grey:#8a99a3;
    --line:#d9e1e5;
  }
  *{box-sizing:border-box;margin:0;padding:0}
  html,body{width:784px;height:1200px;overflow:hidden}
  body{position:relative;background:var(--board);font-family:"Poppins",sans-serif;color:var(--ink)}
  .board-band{position:absolute;inset:0}
  .brand-mark{position:absolute;top:38px;left:0;width:784px;text-align:center;color:var(--white)}
  .brand-mark .square{display:block;width:34px;height:34px;margin:0 auto 10px;border:3px solid var(--white)}
  .brand-mark .name{font-family:"Michroma",sans-serif;font-size:15px;letter-spacing:1px}
  .label{position:absolute;top:142px;font-family:"Michroma",sans-serif;font-size:12px;color:var(--white);letter-spacing:.5px}
  .screen{position:absolute;background:var(--white);overflow:hidden;box-shadow:0 6px 18px rgba(0,0,0,.25)}
  .screen.desktop{left:70px;top:165px;width:314px;height:963px}
  .screen.contact{left:405px;top:165px;width:305px;height:519px;background:var(--paper)}
  .abs{position:absolute}
  /* nav */
  .nav{position:absolute;left:0;top:0;width:100%;height:18px;background:var(--white);display:flex;align-items:center;justify-content:space-between;padding:0 10px;z-index:2}
  .nav .logo{font-family:"Michroma",sans-serif;font-size:4.5px;color:var(--navy);display:flex;align-items:center;gap:3px}
  .nav .logo i{width:6px;height:6px;background:var(--teal);display:block}
  .nav ul{list-style:none;display:flex;gap:7px;font-size:3.6px;color:var(--ink)}
  /* hero */
  .hero-photo{position:absolute;left:0;width:100%}
  .hero-title{font-family:"Michroma",sans-serif;color:var(--white);font-size:15px;line-height:1.25}
  .hero-text{color:#cfe0e6;font-size:4.5px;line-height:1.5}
  .btn{display:inline-block;background:var(--teal);color:var(--white);font-size:4px;padding:3px 8px;font-weight:500}
  .btn.light{background:var(--white);color:var(--teal)}
  .eyebrow{font-size:4px;color:var(--teal);font-weight:500}
  .heading{font-family:"Michroma",sans-serif;color:var(--navy);font-size:8px;line-height:1.3}
  .heading.teal{color:var(--teal)}
  .small{font-size:3.8px;line-height:1.55;color:var(--grey)}
  .feature h4{font-size:4.4px;color:var(--navy);font-weight:600;margin-bottom:2px}
  .center{text-align:center}
  .card{background:var(--white);box-shadow:0 2px 6px rgba(0,0,0,.12)}
  .card h5{font-size:4.2px;color:var(--navy);font-weight:600;padding:4px 5px 1px}
  .card p{padding:0 5px 5px}
  .footer{position:absolute;left:0;width:100%;background:var(--navy)}
  .footer .f-logo{font-family:"Michroma",sans-serif;color:var(--white);font-size:5px;display:flex;align-items:center;gap:4px}
  .footer .f-logo i{width:9px;height:9px;border:1.5px solid var(--white);display:block}
  .footer .col h6{font-size:4.4px;color:var(--white);font-weight:600;margin-bottom:3px}
  .footer .col li{list-style:none;font-size:3.6px;color:#9fb2bd;line-height:1.7}
  .social{display:flex;gap:4px}
  .social span{width:5px;height:5px;border-radius:50%;background:var(--teal-soft);display:block}
  .copyright{font-size:3.4px;color:#6f8794;text-align:center}
  .field{height:11px;border:1px solid var(--line);background:var(--white);font-size:3.6px;color:var(--grey);padding:0 4px;display:flex;align-items:center;margin-bottom:5px}
  .field.area{height:30px;align-items:flex-start;padding-top:3px}
</style>
</head>
<body>

<svg class="board-band" width="784" height="1200" viewBox="0 0 784 1200" aria-hidden="true">
  <polygon points="0,900 784,420 784,650 0,1200" fill="var(--board-light)"/>
</svg>

<header class="brand-mark">
  <span class="square"></span>
  <span class="name">Laurent Dubreuil Conseil</span>
</header>

<span class="label" style="left:70px">DESKTOP</span>
<span class="label" style="left:405px">CONTACT</span>

<!-- Desktop home page -->
<section class="screen desktop">
  <nav class="nav">
    <span class="logo"><i></i>LAURENT DUBREUIL CONSEIL</span>
    <ul><li>HOME</li><li>ABOUT</li><li>SERVICES</li><li>BLOG</li><li>CONTACT</li><li>EN/FR</li></ul>
  </nav>

  <div class="hero-photo" style="top:18px;height:196px;background:linear-gradient(110deg,#0d2535 0%,#1a3d50 45%,#6b7a82 75%,#b9a68e 100%)" role="img" aria-label="Photo of consultants working together at a laptop"></div>
  <svg class="abs" style="left:0;top:180px" width="314" height="36" viewBox="0 0 314 36" aria-hidden="true">
    <polygon points="0,34 0,36 314,36 314,8 210,8 190,34" fill="var(--white)"/>
    <polygon points="0,30 186,30 206,4 314,4 314,8 210,8 190,34 0,34" fill="var(--teal)"/>
  </svg>
  <div class="abs" style="left:14px;top:70px;width:150px">
    <h1 class="hero-title">CONSULTING<br>COMPANY</h1>
    <p class="hero-text" style="margin:6px 0 8px">Data privacy and GDPR advice for growing companies.<br>Clear guidance, secure systems, lasting trust.</p>
    <span class="btn">READ MORE</span>
  </div>

  <!-- About -->
  <div class="abs" style="left:16px;top:232px;width:136px;height:115px;background:linear-gradient(135deg,#0b2a45,#1d5a7a 60%,#3aa6c0)" role="img" aria-label="Illustration of hands on a keyboard with glowing data"></div>
  <div class="abs" style="left:168px;top:250px;width:132px">
    <p class="eyebrow">ABOUT US</p>
    <h2 class="heading" style="margin:3px 0 6px">LAURENT DUBREUIL<br>CONSEIL</h2>
    <p class="small" style="margin-bottom:8px">We help organisations protect personal data, meet GDPR duties and build reliable computer systems. Our team audits, advises and trains your staff step by step.</p>
    <span class="btn">READ MORE</span>
  </div>

  <!-- Privacy access control -->
  <div class="abs center" style="left:0;top:385px;width:314px">
    <h2 class="heading teal">PRIVACY ACCESS CONTROL</h2>
    <p class="small" style="margin-top:3px">Services built around your data protection needs</p>
  </div>
  <div class="abs" style="left:133px;top:430px;width:48px;height:48px;border:5px solid var(--teal)"></div>
  <div class="abs feature" style="left:22px;top:420px;width:100px;text-align:right">
    <h4>DATA MAPPING</h4><p class="small">Full review of the data you collect and store.</p>
  </div>
  <div class="abs feature" style="left:22px;top:460px;width:100px;text-align:right">
    <h4>GDPR AUDIT</h4><p class="small">Gap analysis against current rules and duties.</p>
  </div>
  <div class="abs feature" style="left:192px;top:420px;width:100px">
    <h4>ACCESS RIGHTS</h4><p class="small">Clear roles and controls for every user.</p>
  </div>
  <div class="abs feature" style="left:192px;top:460px;width:100px">
    <h4>STAFF TRAINING</h4><p class="small">Workshops that keep your teams compliant.</p>
  </div>

  <!-- Risk band -->
  <svg class="abs" style="left:0;top:540px" width="314" height="160" viewBox="0 0 314 160" aria-hidden="true">
    <defs>
      <linearGradient id="riskGrad" x1="0" y1="0" x2="1" y2="1">
        <stop offset="0" stop-color="#14808a"/><stop offset="1" stop-color="#27b3a8"/>
      </linearGradient>
    </defs>
    <polygon points="0,14 314,0 314,146 0,160" fill="url(#riskGrad)"/>
  </svg>
  <div class="abs center" style="left:30px;top:582px;width:254px;color:var(--white)">
    <h2 class="heading" style="color:var(--white)">PROBLEM RISK AND IMPACT<br>ASSESSMENT</h2>
    <p class="small" style="color:#d6f0ef;margin:6px 0 8px">We assess privacy risks and the impact of each process before it goes live.</p>
    <span class="btn light">READ MORE</span>
  </div>

  <!-- Blog -->
  <h2 class="abs heading center" style="left:0;top:712px;width:314px">LATEST BLOG</h2>
  <div class="abs card" style="left:22px;top:735px;width:84px">
    <div style="height:44px;background:linear-gradient(135deg,#6a5a4a,#b59b7c)" role="img" aria-label="Blog photo of people in a meeting"></div>
    <h5>GDPR CHECKLIST</h5><p class="small">Key steps for a first audit.</p>
  </div>
  <div class="abs card" style="left:115px;top:735px;width:84px">
    <div style="height:44px;background:linear-gradient(135deg,#2a3c4c,#7d8a94)" role="img" aria-label="Blog photo of a person typing on a laptop"></div>
    <h5>SECURE ACCESS</h5><p class="small">Simple rules for user rights.</p>
  </div>
  <div class="abs card" style="left:208px;top:735px;width:84px">
    <div style="height:44px;background:linear-gradient(135deg,#0d2c6a,#2f78c8)" role="img" aria-label="Blog illustration of digital security"></div>
    <h5>DATA BREACHES</h5><p class="small">How to react in the first hours.</p>
  </div>

  <!-- Footer -->
  <svg class="abs" style="left:0;top:822px" width="314" height="20" viewBox="0 0 314 20" aria-hidden="true">
    <polygon points="0,0 120,0 140,20 0,20" fill="var(--navy)"/>
    <polygon points="0,14 314,14 314,20 0,20" fill="var(--navy)"/>
  </svg>
  <footer class="footer" style="top:840px;height:123px;padding:14px 16px">
    <div class="abs" style="left:16px;top:24px">
      <span class="f-logo"><i></i>LAURENT DUBREUIL<br>CONSEIL</span>
      <div class="social" style="margin-top:8px"><span></span><span></span><span></span></div>
    </div>
    <div class="abs col" style="left:130px;top:16px"><h6>SERVICES</h6><ul><li>Data audit</li><li>GDPR advice</li><li>Training</li><li>IT security</li></ul></div>
    <div class="abs col" style="left:190px;top:16px"><h6>CONTACT</h6><ul><li>Paris, France</li><li>+33 1 00 00 00</li><li>hello@ldconseil.fr</li></ul></div>
    <div class="abs col" style="left:255px;top:16px"><h6>SUPPORT</h6><ul><li>Privacy policy</li><li>Legal notice</li><li>Cookies</li></ul></div>
    <p class="abs copyright" style="left:0;bottom:8px;width:314px">© Laurent Dubreuil Conseil. All rights reserved.</p>
  </footer>
</section>

<!-- Contact page -->
<section class="screen contact">
  <nav class="nav">
    <span class="logo"><i></i>LAURENT DUBREUIL CONSEIL</span>
    <ul><li>HOME</li><li>ABOUT</li><li>SERVICES</li><li>BLOG</li><li>CONTACT</li></ul>
  </nav>
  <div class="hero-photo" style="top:18px;height:92px;background:linear-gradient(110deg,#0b2232,#163a4c 60%,#24566a)" role="img" aria-label="Dark photo of an office workspace"></div>
  <svg class="abs" style="left:0;top:88px" width="305" height="24" viewBox="0 0 305 24" aria-hidden="true">
    <polygon points="0,24 0,10 170,10 190,24" fill="var(--paper)"/>
    <polygon points="190,24 210,6 305,6 305,24" fill="var(--paper)"/>
    <polygon points="0,6 172,6 192,20 188,22 170,10 0,10" fill="var(--teal)"/>
  </svg>
  <h1 class="abs hero-title center" style="left:0;top:46px;width:305px;font-size:11px">CONTACT</h1>

  <div class="abs card" style="left:78px;top:136px;width:144px;height:261px;padding:14px 12px">
    <p class="eyebrow center">GET IN TOUCH</p>
    <h2 class="heading center" style="font-size:6.5px;margin:3px 0 12px">CONNECTING WITH US</h2>
    <div class="field">Full name</div>
    <div class="field">Email address</div>
    <div class="field">Phone</div>
    <div class="field">Company</div>
    <div class="field">Subject</div>
    <div class="field area">Your message</div>
    <div class="btn" style="display:block;text-align:center;margin-top:10px">SEND MESSAGE</div>
  </div>

  <svg class="abs" style="left:0;top:406px" width="305" height="18" viewBox="0 0 305 18" aria-hidden="true">
    <polygon points="180,0 305,0 305,18 160,18" fill="var(--navy)"/>
    <polygon points="0,12 305,12 305,18 0,18" fill="var(--navy)"/>
  </svg>
  <footer class="footer" style="top:423px;height:96px">
    <div class="abs" style="left:16px;top:16px">
      <span class="f-logo"><i></i>LAURENT DUBREUIL<br>CONSEIL</span>
      <div class="social" style="margin-top:8px"><span></span><span></span><span></span></div>
    </div>
    <div class="abs col" style="left:126px;top:12px"><h6>SERVICES</h6><ul><li>Data audit</li><li>GDPR advice</li><li>Training</li></ul></div>
    <div class="abs col" style="left:186px;top:12px"><h6>CONTACT</h6><ul><li>Paris, France</li><li>+33 1 00 00 00</li></ul></div>
    <div class="abs col" style="left:250px;top:12px"><h6>SUPPORT</h6><ul><li>Privacy policy</li><li>Legal notice</li></ul></div>
    <p class="abs copyright" style="left:0;bottom:7px;width:305px">© Laurent Dubreuil Conseil. All rights reserved.</p>
  </footer>
</section>

</body>
</html>
```